Q-Rolls Business Card

We are a modern retail clothing store. Established in 1994. I need a presentable card that will amaze vendors when given to them.

Front: Logo in middle
Info Side:

Name: Tomas Velder
Cell: 630-812-4463
Work: 630-917-3384 EXT. 417
Email: Tomas@q-rolls-example.com
Website: www.Q-rolls-example.com

Industry/Entity Type

Business

```html
<!DOCTYPE html>
<html lang="en">
<head>
<meta charset="utf-8">
<title>Q-Rolls Business Card</title>
<link rel="stylesheet" href="https://fonts.googleapis.com/css2?family=Michroma&family=Arimo:wght@400&display=swap">
<style>
  :root {
    --backdrop: #dcd8d1;
    --card-white: #ffffff;
    --card-black: #050505;
    --band-gray: #8a8a8a;
    --ink: #0a0a0a;
    --ink-light: #ffffff;
  }
  * { box-sizing: border-box; margin: 0; padding: 0; }
  html, body {
    width: 1200px;
    height: 892px;
    overflow: hidden;
    background: var(--backdrop);
  }
  .stage {
    position: relative;
    width: 1200px;
    height: 892px;
  }
  .card {
    position: absolute;
    top: 148px;
    width: 340px;
    height: 595px;
    background: var(--card-white);
    box-shadow: 0 6px 18px rgba(0,0,0,0.25);
    overflow: hidden;
  }
  .card--info { left: 190px; }
  .card--front { left: 670px; }

  .card__waves {
    position: absolute;
    inset: 0;
    width: 100%;
    height: 100%;
  }
  .wave--band { fill: var(--band-gray); }
  .wave--base { fill: var(--card-black); }

  .brand-name {
    font-family: "Michroma", sans-serif;
    color: var(--ink);
    white-space: nowrap;
  }
  .card--info .brand-name {
    position: absolute;
    top: 92px;
    left: 0;
    width: 100%;
    text-align: center;
    font-size: 46px;
    letter-spacing: 1px;
  }
  .card--front .brand-name {
    position: absolute;
    top: 50%;
    left: 50%;
    font-size: 78px;
    letter-spacing: 2px;
    transform: translate(-50%, -50%) rotate(90deg);
  }

  .contact {
    position: absolute;
    left: 0;
    top: 368px;
    width: 100%;
    text-align: center;
    color: var(--ink-light);
  }
  .contact__name {
    font-family: "Michroma", sans-serif;
    font-size: 24px;
    margin-bottom: 22px;
  }
  .contact__line {
    font-family: "Arimo", sans-serif;
    font-size: 17px;
    line-height: 27px;
  }
</style>
</head>
<body>
  <main class="stage">
    <section class="card card--info" aria-label="Card info side">
      <svg class="card__waves" viewBox="0 0 340 595" preserveAspectRatio="none" aria-hidden="true">
        <path class="wave--band" d="M0,222 C110,210 160,310 340,282 L340,595 L0,595 Z"/>
        <path class="wave--base" d="M0,238 C110,226 160,326 340,298 L340,595 L0,595 Z"/>
      </svg>
      <div class="brand-name">Q-Rolls</div>
      <div class="contact">
        <p class="contact__name">Tomas Velder</p>
        <p class="contact__line">630-812-4463</p>
        <p class="contact__line">630-917-3384 EXT. 417</p>
        <p class="contact__line">Tomas@q-rolls-example.com</p>
        <p class="contact__line">www.Q-rolls-example.com</p>
      </div>
    </section>

    <section class="card card--front" aria-label="Card front">
      <div class="brand-name">Q-Rolls</div>
    </section>
  </main>
</body>
</html>
```